Coaching business needs flyer for business market

I need a flyer that I can send to HR-managers and business owners to inform them of my coaching services for organisations. We have three services: organisational- and teamcoaching, individual coaching and training programs.
I want the flyer to express calmness, solid and trustworthy coaching. As a person I am open and think out of the box.

In my logo I use a couple of colours (blue, green, orange and grey) that represent the diversity of humans. My company's name is Bramblecrest Engagement & Coaching and tag line is "Awaken your quiet river".

I do not want the design to be too busy but also not too boring. I tried making something myself. Feel free to build on that design. Or feel free to start from scratch.

```html
<!DOCTYPE html>
<html lang="nl">
<head>
<meta charset="utf-8">
<title>Bramblecrest Engagement &amp; Coaching – flyer</title>
<link rel="stylesheet" href="https://fonts.googleapis.com/css2?family=Poppins:wght@300;400;500;600;700;800&family=Dancing+Script:wght@700&family=Kalam:wght@400&display=swap">
<style>
:root{
  --stage:#c6c6c6;
  --paper:#f2f3f4;
  --paper-shade:#e4e7e9;
  --charcoal:#5a5a5a;
  --charcoal-soft:#7c7c7c;
  --ink:#3a3a3a;
  --brand-grey:#5f6468;
  --red:#c8462e;
  --blue:#1f6fa0;
  --blue-bright:#3a9ad3;
  --orange:#f0961e;
  --teal:#8fcfc2;
  --white:#ffffff;
}
*{margin:0;padding:0;box-sizing:border-box}
html,body{width:971px;height:1200px;overflow:hidden;background:var(--stage)}
.flyer{
  position:absolute;left:106px;top:101px;width:765px;height:989px;overflow:hidden;
  background:radial-gradient(ellipse at 30% 20%,#fafbfc 0%,var(--paper) 55%,var(--paper-shade) 100%);
  font-family:"Poppins",sans-serif;color:var(--ink);
}
.flyer-shapes{position:absolute;inset:0}
.brand{position:absolute;left:30px;top:78px;width:230px;text-align:center;color:var(--brand-grey);font-weight:500}
.brand-name{font-size:26px;line-height:32px}
.brand-sub{font-size:14px;line-height:20px;margin-top:4px}
.coach-name{position:absolute;left:397px;top:28px;font-family:"Dancing Script",cursive;font-size:27px;color:var(--white);font-weight:700}
.coach-bio{position:absolute;left:396px;top:63px;font-size:9.6px;line-height:12px;font-weight:300;color:var(--white);white-space:nowrap;letter-spacing:-.1px}
.service-title{position:absolute;font-weight:800;font-size:23.8px;line-height:30px;letter-spacing:-.2px}
.service-title.org{left:345px;top:232px;color:var(--red)}
.service-title.individual{left:51px;top:453px;color:var(--blue)}
.service-title.training{left:345px;top:676px;color:var(--orange)}
.service-list{position:absolute;list-style:none}
.service-list li{height:27.4px;display:flex;align-items:center;font-size:12.7px;font-weight:600;color:var(--ink);white-space:nowrap}
.service-list .q{width:19px;height:19px;border-radius:50%;margin-right:7px;flex:none;font-size:12px;font-weight:700;display:flex;align-items:center;justify-content:center;box-shadow:0 0 0 2px var(--white),0 0 0 3px currentColor}
.service-list .q::after{content:"?";color:var(--white)}
.service-list.org{left:345px;top:296px}
.service-list.org .q{background:var(--red);color:var(--red)}
.service-list.individual{left:52px;top:487px}
.service-list.individual .q{background:var(--blue);color:var(--blue)}
.service-list.training{left:345px;top:713px}
.service-list.training .q{background:var(--orange);color:var(--orange)}
.service-list li.plain{padding-left:26px}
.promise{position:absolute;left:47px;top:894px;color:var(--white);font-weight:700;font-size:16px;line-height:21px}
.promise .script{font-family:"Kalam",cursive;font-weight:400;font-size:20px;margin-left:4px}
.methods{position:absolute;left:365px;top:895px;list-style:none;color:var(--white);font-size:10.4px;line-height:14.7px;font-weight:400}
.methods li{padding-left:14px;position:relative}
.methods li::before{content:"";position:absolute;left:1px;top:4px;width:6px;height:6px;border:1px solid var(--white);transform:rotate(45deg)}
.methods li.cont::before{display:none}
.methods b{font-weight:600}
</style>
</head>
<body>
<main class="flyer">
  <svg class="flyer-shapes" width="765" height="989" viewBox="0 0 765 989">
    <defs>
      <linearGradient id="charcoalFade" x1="0" y1="0" x2="1" y2="0">
        <stop offset="0" stop-color="#555"/><stop offset="1" stop-color="#6a6a6a"/>
      </linearGradient>
      <linearGradient id="bandFade" x1="0" y1="0" x2="1" y2="1">
        <stop offset="0" stop-color="#3a9ad3"/><stop offset=".5" stop-color="#1f6fa0"/><stop offset="1" stop-color="#2a86bf"/>
      </linearGradient>
    </defs>
    <!-- header band -->
    <path d="M250,0 L765,0 L765,236 C700,222 640,212 560,205 C480,198 420,218 370,215 C335,212 318,190 325,160 Z" fill="var(--charcoal-soft)"/>
    <path d="M235,0 L765,0 L765,220 C700,200 640,185 560,190 C470,195 420,212 375,206 C340,200 328,180 325,155 C300,120 260,95 250,50 Z" fill="url(#charcoalFade)"/>
    <circle cx="322" cy="84" r="61" fill="#4a5550"/>
    <path d="M261,84 A61,61 0 0 0 322,145 L322,137 A53,53 0 0 1 269,84Z" fill="var(--teal)"/>
    <circle cx="322" cy="84" r="55" fill="var(--white)"/>
    <circle cx="322" cy="84" r="52" fill="#4a5fb0" role="img" aria-label="Portrait of coach Marisol Vandenberg smiling"/>

    <!-- organisational photo -->
    <path d="M235,203 C140,196 52,248 52,325 C52,385 100,418 160,426" fill="none" stroke="var(--red)" stroke-width="5"/>
    <path d="M62,330 C57,250 120,207 200,207 C260,208 300,240 285,285 C278,320 325,360 312,395 C292,428 220,426 170,420 C100,410 64,380 62,330Z" fill="#9a7a62" role="img" aria-label="Team exercise: group standing around a floor map in a meeting room"/>

    <!-- individual photo -->
    <path d="M610,430 C700,432 752,490 742,560 C736,595 715,620 690,635" fill="none" stroke="var(--blue)" stroke-width="7"/>
    <path d="M500,465 C525,430 610,425 690,448 C745,475 740,560 712,600 C675,643 585,650 533,622 C482,592 470,505 500,465Z" fill="#9c9287" role="img" aria-label="Individual coaching session in a bright room"/>

    <!-- training photo -->
    <path d="M150,660 C200,640 240,640 270,650 C300,660 320,660 330,690 C340,720 330,770 310,810" fill="none" stroke="var(--orange)" stroke-width="7"/>
    <path d="M40,740 C40,685 110,658 190,662 C235,664 270,648 300,665 C328,692 322,760 302,800 C272,845 185,850 122,832 C62,812 40,782 40,740Z" fill="#25243a" role="img" aria-label="Training group seated in a circle in a dimly lit hall"/>

    <!-- bottom band -->
    <path d="M0,838 C120,845 220,875 280,878 C400,882 520,838 640,852 C700,860 740,880 765,890 L765,989 L0,989Z" fill="url(#bandFade)"/>
    <path d="M0,848 C90,848 180,860 260,878" fill="none" stroke="var(--white)" stroke-width="4"/>
    <path d="M560,850 C640,848 710,880 765,905" fill="none" stroke="var(--blue-bright)" stroke-width="5" opacity=".8"/>
    <path d="M540,852 C630,852 705,890 765,915" fill="none" stroke="var(--white)" stroke-width="2" opacity=".6"/>
  </svg>

  <div class="brand">
    <div class="brand-name">Bramblecrest</div>
    <div class="brand-sub">Engagement &amp; Coaching</div>
  </div>

  <h2 class="coach-name">Marisol Vandenberg</h2>
  <p class="coach-bio">is trainer en coach. Ze heeft ruime ervaring met veranderingstrajecten<br>binnen organisaties. Mensen omschrijven haar als ‘betrokken, warm,<br>stevig en kordaat’. Het is haar passie om organisaties, teams en mensen<br>te helpen groeien. Zij helpt weerstand te overwinnen en draagt bij aan<br>groei in zelfvertrouwen. Haar trainingen en coaching zijn erop gericht om<br>snel inzichtelijk te krijgen welke stappen men moet zetten om verder te<br>komen. Ze gelooft de veranderkracht van de mensen waar ze mee werkt.<br>Ze is er om steun en richting te bieden en laat hen zelf aan het roer.</p>

  <h1 class="service-title org">ORGANISATIONAL AND<br>TEAMCOACHING</h1>
  <ul class="service-list org">
    <li><span class="q"></span>Heb je zorgen voor of na een fusie of verandering?</li>
    <li><span class="q"></span>Wil je missie, visie &amp; strategie ontwikkelen of wijzigen?</li>
    <li><span class="q"></span>Wens je de cultuur-veranderen of verder ontwikkelen?</li>
    <li><span class="q"></span>Beoog je de samenwerking bevorderen of verbeteren?</li>
  </ul>

  <h1 class="service-title individual">INDIVIDUAL COACHING</h1>
  <ul class="service-list individual">
    <li><span class="q"></span>Wens je medewerkers die hun talent ten volste benutten?</li>
    <li><span class="q"></span>Verlang je meer authentieke leiderschap bij je collega’s?</li>
    <li><span class="q"></span>Wil je de mensen vooruit helpen in hun loopbaan?</li>
    <li><span class="q"></span>Zoek je steun voor medewerkers met burn-out of re-integratie?</li>
    <li class="plain">Heb je hulp nodig bij outplacement trajecten?</li>
  </ul>

  <h1 class="service-title training">TRAINING PROGRAMS</h1>
  <ul class="service-list training">
    <li><span class="q"></span>Leiderschap</li>
    <li><span class="q"></span>Communicatie</li>
    <li><span class="q"></span>Leren kijken met ‘systemische blik’ voor professionals</li>
    <li><span class="q"></span>Conflicthantering</li>
  </ul>

  <p class="promise">Gedegen resultaat en kwaliteit door<br>bewezen <span class="script">‘best practices’</span></p>
  <ul class="methods">
    <li>Neuro Linguïstisch Programmeren (NLP)</li>
    <li>Transactionele Analyse</li>
    <li><b>Systemisch Werken:</b> Organisatieopstellingen,</li>
    <li class="cont">Familieopstellingen, Identity oriented Psycho Traumaopstellingen)</li>
    <li>Somatic Experience, Ademwerk en Lichaamswerk</li>
  </ul>
</main>
</body>
</html>
```